Brivanta.com the Free Online Tutorial Needs a New Web Design

We need a new web design for our existing website, Brivanta.com. We provide a Free Online Tutorial of any code, like HTML, CSS, PHP, QueryKit, javascript etc, including online editor.
We would like to see designs that interesting, simple, interactive, and be a very comfortable place to read in a long time.
We need 2 pages design for:
1. Home Page (http://brivanta.com) and
2. Listing Page (http://brivanta.com/tutorial/833/sql/sql-basics/sql-and-or-operator.html)
For Listing Page We need nice "Left Menu" at left side and Content Page (min 728px) at right side.
I need File PSD and/or Vector Only, without HTML code.
Online
2 page

```html
<!DOCTYPE html>
<html lang="en">
<head>
<meta charset="utf-8">
<title>Brivanta – A Place for Learning and Trying of any Code</title>
<link rel="stylesheet" href="https://fonts.googleapis.com/css2?family=Yanone+Kaffeesatz:wght@300;400;600&family=Lato:wght@400;700&display=swap">
<style>
:root{
  --red:#f25450;
  --blue:#1b77c9;
  --green:#6cb33f;
  --yellow:#fbb610;
  --grey:#666666;
  --ink:#222222;
  --black:#111111;
  --paper:#ffffff;
  --tile:#e9e9e9;
  --line:#cfcfcf;
  --head:"Yanone Kaffeesatz",sans-serif;
  --body:"Lato",sans-serif;
}
*{box-sizing:border-box;margin:0;padding:0}
html,body{width:759px;height:1200px;overflow:hidden;background:var(--paper)}
body{font-family:var(--body);color:var(--ink);position:relative}
a{color:inherit;text-decoration:none}
ul{list-style:none}

/* header */
.site-header{position:absolute;left:0;top:0;width:759px;height:59px}
.brand{position:absolute;left:83px;top:13px;display:flex;align-items:center;gap:6px}
.brand-mark{width:26px;height:28px;background:var(--blue)}
.brand-name{font-family:var(--head);font-weight:600;font-size:34px;line-height:30px;color:var(--ink)}
.tagline{position:absolute;left:231px;top:32px;font-size:11.5px;font-weight:700;color:var(--green)}
.account{position:absolute;right:83px;top:8px;display:flex;gap:6px}
.account a{display:block;height:17px;padding:0 7px;font-size:8.5px;line-height:17px;border-radius:2px}
.btn-login{background:var(--yellow);color:var(--ink)}
.btn-register{background:var(--green);color:#fff}
.site-search{position:absolute;left:519px;top:31px;display:flex}
.site-search span{width:136px;height:18px;border:1px solid #999;font-size:7.5px;line-height:16px;padding-left:5px;color:#333}
.site-search b{width:21px;height:18px;background:var(--black);display:flex;align-items:center;justify-content:center}

/* nav */
.main-nav{position:absolute;left:0;top:59px;width:759px;height:30px;background:var(--red)}
.main-nav ul{position:absolute;left:83px;top:0;display:flex;height:30px}
.main-nav li{font-family:var(--head);font-size:14px;line-height:30px;color:#fff;padding:0 10px;border-right:1px solid rgba(255,255,255,.25)}
.main-nav li.current{background:var(--blue);padding:0 14px}
.main-nav li:last-child{border-right:0}
.try-it{position:absolute;right:83px;top:0;width:42px;height:30px;background:var(--green);font-family:var(--head);font-size:14px;line-height:30px;text-align:center;color:#fff}

/* hero */
.hero{position:absolute;left:0;top:89px;width:759px;height:207px;background:radial-gradient(ellipse at 62% 55%,#6d6a66 0%,#3b3937 40%,#1a1918 75%),#222}
.hero h1{position:absolute;left:0;top:40px;width:759px;text-align:center;font-family:var(--head);font-weight:400;font-size:31px;line-height:32px;color:#fff}
.hero-cta{position:absolute;left:326px;top:120px;width:107px;height:32px;background:var(--yellow);font-family:var(--head);font-size:19px;line-height:32px;text-align:center;color:var(--ink)}
.hero-dots{position:absolute;left:346px;top:182px;display:flex;gap:6px}
.hero-dots i{width:12px;height:12px;border-radius:50%;background:#bbb}
.hero-dots i.on{background:var(--red)}

/* section headings */
.section-title{position:absolute;left:0;width:759px;text-align:center;font-family:var(--head);font-weight:400;font-size:26px;color:var(--ink)}
.section-sub{position:absolute;left:0;width:759px;text-align:center;font-size:11px;color:var(--red)}

/* tutorials */
.course-card{position:absolute;width:141px;height:128px;border:1px solid var(--ink);background:#fff}
.course-mark{position:absolute;left:50px;top:18px;width:40px;height:46px}
.course-mark.round{border-radius:50%;width:44px;height:44px;left:48px}
.course-title{position:absolute;left:0;top:79px;width:139px;text-align:center;font-family:var(--head);font-size:14px;color:var(--ink)}
.course-title em{font-style:normal;margin-right:4px}
.course-label{position:absolute;left:-1px;bottom:-1px;width:141px;height:26px;background:#2a2a2a;color:#fff;font-family:var(--head);font-size:12.5px;line-height:26px;text-align:center}
.row2 .course-title{top:71px}

/* intro band */
.intro{position:absolute;left:0;top:677px;width:759px;height:110px;background:var(--green);border-top:2px solid #a8a8a8;border-bottom:2px solid #a8a8a8;text-align:center;color:#fff}
.intro h2{font-family:var(--head);font-weight:400;font-size:26px;margin-top:14px}
.intro p{width:570px;margin:6px auto 0;font-size:9.6px;line-height:13px}

/* tryit tiles */
.tryit-card{position:absolute;top:859px;width:143px;height:82px}
.tryit-top{height:58px;background:var(--tile);position:relative}
.tryit-mark{position:absolute;left:22px;top:12px;width:36px;height:36px;background:#888}
.tryit-text{position:absolute;left:71px;top:11px;font-size:9px;line-height:12.5px}
.tryit-text small{display:block;color:var(--ink);font-weight:700;font-size:7.5px}
.tryit-label{height:24px;background:var(--black);color:#fff;font-family:var(--head);font-size:12.5px;line-height:24px;text-align:center}

/* link columns */
.link-columns{position:absolute;left:83px;top:967px;width:593px;height:191px;display:flex}
.link-col{height:191px;padding:10px 0 0 8px;color:#fff}
.link-col h3{font-family:var(--head);font-weight:400;font-size:12.5px;margin-bottom:6px}
.link-col li{font-size:7.6px;line-height:15.4px;white-space:nowrap;overflow:hidden;text-overflow:ellipsis}
.link-col li::before{content:"• "}

/* footer */
.site-footer{position:absolute;left:0;top:1158px;width:759px;height:42px;background:var(--black);color:#fff}
.footer-links{position:absolute;left:83px;top:7px;font-family:var(--head);font-size:11px;line-height:15px;width:190px}
.footer-links a{margin-right:4px}
.footer-links a.current{color:var(--red)}
.footer-search{position:absolute;left:314px;top:11px;display:flex}
.footer-search span{width:136px;height:20px;background:#fff;color:#333;font-size:7.5px;line-height:20px;padding-left:5px}
.footer-search b{width:20px;height:20px;background:var(--red);display:flex;align-items:center;justify-content:center}
.follow{position:absolute;right:83px;top:6px;display:flex;align-items:center;gap:6px;font-family:var(--head);font-size:11px}
.follow i{width:14px;height:14px;background:#4a4a4a}
.follow .store{width:46px;background:#2d2d2d}
.copyright{position:absolute;right:83px;top:26px;font-family:var(--head);font-size:10.5px}
</style>
</head>
<body>

<header class="site-header">
  <a class="brand" href="#"><span class="brand-mark"></span><span class="brand-name">Brivanta</span></a>
  <p class="tagline">A Place for Learning and Trying of any Code</p>
  <div class="account"><a class="btn-login" href="#">Login</a><a class="btn-register" href="#">Register</a></div>
  <form class="site-search"><span>Search by Findwell Engine..</span><b><svg width="13" height="13" viewBox="0 0 13 13"><circle cx="5.5" cy="5.5" r="4" fill="none" stroke="#fff" stroke-width="1.6"/><line x1="8.5" y1="8.5" x2="12" y2="12" stroke="#fff" stroke-width="1.8"/></svg></b></form>
</header>

<nav class="main-nav">
  <ul>
    <li class="current">HOME</li><li>HTML</li><li>CSS</li><li>JAVASCRIPT</li><li>PHP</li><li>SQL</li><li>QUERYKIT</li><li>JSON</li><li>MORE..</li>
  </ul>
  <a class="try-it" href="#">TRY IT</a>
</nav>

<section class="hero" role="img" aria-label="Photo of a laptop on a wooden desk in a dim room">
  <h1>Lorem ipsum dolor sit amet consectetuer<br>adipiscing elit sed diam nonummy nibh</h1>
  <a class="hero-cta" href="#">GET STARTED</a>
  <div class="hero-dots"><i></i><i class="on"></i><i></i><i></i></div>
</section>

<h2 class="section-title" style="top:316px">Tutorials Library</h2>
<p class="section-sub" style="top:347px">Free Online Tutorials &amp; Courses</p>

<div class="course-card" style="left:83px;top:376px"><span class="course-mark" style="background:#e44d26"></span><p class="course-title"><em style="color:#e44d26">HTML5</em>Brivanta</p><p class="course-label">HTML5 Tutorial</p></div>
<div class="course-card" style="left:234px;top:376px"><span class="course-mark" style="background:#1572b6"></span><p class="course-title"><em style="color:#1572b6">CSS3</em>Brivanta</p><p class="course-label">CSS3 Tutorial</p></div>
<div class="course-card" style="left:384px;top:376px"><span class="course-mark" style="background:#e8a530"></span><p class="course-title"><em style="color:#e8a530">Javascript</em>Brivanta</p><p class="course-label">Javascript Tutorial</p></div>
<div class="course-card" style="left:535px;top:376px"><span class="course-mark round" style="background:#6a72b5"></span><p class="course-title"><em style="color:#6a72b5">PHP</em>Brivanta</p><p class="course-label">PHP Tutorial</p></div>

<div class="course-card row2" style="left:83px;top:524px"><span class="course-mark" style="background:#1e3a6b"></span><p class="course-title"><em style="color:#1e3a6b">SQL</em>Brivanta</p><p class="course-label">SQL Tutorial</p></div>
<div class="course-card row2" style="left:234px;top:524px"><span class="course-mark round" style="background:#2aa3da"></span><p class="course-title"><em style="color:#2aa3da">QUERYKIT</em>Brivanta</p><p class="course-label">QueryKit Tutorial</p></div>
<div class="course-card row2" style="left:384px;top:524px"><span class="course-mark" style="background:#1f5f7a"></span><p class="course-title"><em style="color:#1f5f7a">QUILLDB</em>Brivanta</p><p class="course-label">QuillDB Tutorial</p></div>
<div class="course-card row2" style="left:535px;top:524px"><span class="course-mark round" style="background:#333"></span><p class="course-title"><em>JSON</em>Brivanta</p><p class="course-label">JSON Tutorial</p></div>

<section class="intro">
  <h2>The Free Online Tutorials Place</h2>
  <p>Brivanta is a place for Learning, testing, and examples for web building. The Examples in each chapter might be simplified to improve your basic understanding. With Brivanta You will feel much easier than ever to learn about HTML including online code editor for each chapter, so you can edit, modify and execute the code.</p>
</section>

<h2 class="section-title" style="top:807px">Featured Tryit Yourself</h2>

<div class="tryit-card" style="left:83px"><div class="tryit-top"><span class="tryit-mark"></span><p class="tryit-text" style="color:var(--blue)">HTML 5<br>Try it Yourself<small>Brivanta</small></p></div><p class="tryit-label">HTML5 Examples</p></div>
<div class="tryit-card" style="left:233px"><div class="tryit-top"><span class="tryit-mark"></span><p class="tryit-text" style="color:var(--green)">HTML 5 CANVAS<br>Try it Yourself<small>Brivanta</small></p></div><p class="tryit-label">Canvas Examples</p></div>
<div class="tryit-card" style="left:383px"><div class="tryit-top"><span class="tryit-mark"></span><p class="tryit-text" style="color:var(--red)">SQL<br>Try it Yourself<small>Brivanta</small></p></div><p class="tryit-label">SQL Examples</p></div>
<div class="tryit-card" style="left:533px"><div class="tryit-top"><span class="tryit-mark"></span><p class="tryit-text" style="color:var(--yellow)">Online Code<br>Try it Yourself<small>Brivanta</small></p></div><p class="tryit-label">Online Code Editor</p></div>

<section class="link-columns">
  <div class="link-col" style="width:116px;background:var(--blue)"><h3>Random HTML5</h3><ul><li>Time Tag In Html5</li><li>P In Html5</li><li>Col Tag In Html</li><li>Progress In Html5</li><li>Text Formating Overview I..</li><li>I Tag In Html5</li><li>Command</li><li>Rp In Html5</li><li>Q Tag In Html5</li><li>Footer In Html5</li></ul></div>
  <div class="link-col" style="width:109px;background:var(--green)"><h3>Random Canvas</h3><ul><li>Canvas Custom Paths</li><li>Canvas Line Join</li><li>Canvas Image Crop</li><li>Canvas Fill Style</li><li>Canvas Quadratic Curve</li><li>Canvas Introduction</li><li>Canvas Semicircles</li><li>Canvas Text Basics</li><li>Canvas Line Cap</li><li>Canvas Pattern</li></ul></div>
  <div class="link-col" style="width:124px;background:var(--red)"><h3>Random Javascript</h3><ul><li>Javascript Browser Window</li><li>JS Global unescape()</li><li>JS Global Function eval()</li><li>Javascript Operators</li><li>JS RegExp ignoreCase</li><li>Javascript Variables</li><li>JS DOM Body Object</li><li>JS DOM Frameset Object</li><li>Javascript Comparison - L..</li><li>Javascript Browser Compat..</li></ul></div>
  <div class="link-col" style="width:116px;background:var(--yellow)"><h3>Random Try it</h3><ul><li>HTML Symbols Examples</li><li>Colors RGB in HTML</li><li>progress tag without valu..</li><li>title tag example</li><li>iframe tag Example</li><li>colgroup tag example</li><li>ins tag example</li><li>External Style Sheet CSS..</li><li>hr tag example</li><li>h2 tag example</li></ul></div>
  <div class="link-col" style="width:128px;background:var(--grey)"><h3>Random Articles</h3><ul><li>How to Auto Select All Te..</li><li>How to Make Sitemap.xml</li><li>How to Make Drop Down Men..</li><li>How to make WHOIS lookups..</li><li>How to get an input text ..</li><li>Changing text with innerh..</li><li>Make A lot of Circle Anim..</li><li>How to Make SQL Syntax Hi..</li><li>Create Transparency Anima..</li><li>How to Make Drop Down Men..</li></ul></div>
</section>

<footer class="site-footer">
  <nav class="footer-links"><a class="current" href="#">Tutorial</a> <a href="#">Articles</a> <a href="#">Try it</a> <a href="#">Canvas</a> <a href="#">Webtools</a><br><a href="#">About</a> <a href="#">Terms</a> <a href="#">Privacy</a> <a href="#">Disclaimer</a> <a href="#">Contact</a> <a href="#">FAQ</a></nav>
  <form class="footer-search"><span>Search by Brivanta..</span><b><svg width="13" height="13" viewBox="0 0 13 13"><circle cx="5.5" cy="5.5" r="4" fill="none" stroke="#fff" stroke-width="1.6"/><line x1="8.5" y1="8.5" x2="12" y2="12" stroke="#fff" stroke-width="1.8"/></svg></b></form>
  <div class="follow">Find Us on <i></i><i></i><i class="store"></i></div>
  <p class="copyright">© 2015 Brivanta. All Rights Reserved.</p>
</footer>

</body>
</html>
```